Business Cards for a Dating Coach/Social Dynamics company
Velvet Compass
Professional
Ted
Dating Instructor
4872 Marlow Terrace, #9
Miami Beach, FL 33139
Skyheron@velvetcompasslife.com
www.velvetcompasslife.com

```html
<!DOCTYPE html>
<html lang="en">
<head>
<meta charset="utf-8">
<title>Velvet Compass – Business Card</title>
<link rel="stylesheet" href="https://fonts.googleapis.com/css2?family=Open+Sans:wght@400;600&display=swap">
<style>
  :root {
    --page-bg: #e9e7e4;
    --card-bg: #4b4c4e;
    --strip-bg: #6a6b6d;
    --accent-red: #e0301e;
    --accent-orange: #f07a1a;
    --text-light: #e6e6e6;
    --text-muted: #cfcfcf;
  }
  html, body {
    margin: 0;
    padding: 0;
    width: 1200px;
    height: 900px;
    overflow: hidden;
    background: var(--page-bg);
    font-family: "Open Sans", Arial, sans-serif;
  }
  .canvas {
    position: relative;
    width: 1200px;
    height: 900px;
  }
  .business-card {
    position: absolute;
    left: 100px;
    top: 165px;
    width: 1000px;
    height: 570px;
    background: var(--card-bg);
    box-shadow: 0 6px 18px rgba(0,0,0,0.18);
    overflow: hidden;
  }
  .side-strip {
    position: absolute;
    top: 0;
    right: 0;
    width: 118px;
    height: 100%;
    background: var(--strip-bg);
  }
  .side-strip-line {
    position: absolute;
    top: 24px;
    left: 0;
    width: 3px;
    height: 300px;
    background: var(--accent-red);
  }
  .side-strip-url {
    position: absolute;
    top: 50px;
    left: 50%;
    writing-mode: vertical-rl;
    transform: translateX(-50%) rotate(180deg);
    font-size: 20px;
    letter-spacing: 2px;
    color: var(--text-light);
    white-space: nowrap;
  }
  .brand {
    position: absolute;
    left: 70px;
    top: 148px;
    display: flex;
    align-items: center;
    gap: 18px;
  }
  .brand-mark {
    width: 62px;
    height: 62px;
    border-radius: 50%;
    background: var(--accent-red);
    flex: none;
  }
  .brand-name {
    font-size: 44px;
    font-weight: 600;
    color: var(--accent-red);
    line-height: 1;
    white-space: nowrap;
  }
  .brand-tagline {
    position: absolute;
    left: 150px;
    top: 222px;
    font-size: 16px;
    letter-spacing: 1.5px;
    text-transform: uppercase;
    color: var(--text-light);
    white-space: nowrap;
  }
  .person {
    position: absolute;
    left: 0;
    top: 300px;
  }
  .person-marker {
    position: absolute;
    left: 0;
    top: 18px;
  }
  .person-name {
    margin: 0 0 4px 40px;
    font-size: 18px;
    font-weight: 600;
    color: var(--accent-orange);
  }
  .person-title {
    margin: 0 0 0 40px;
    font-size: 19px;
    color: var(--text-light);
  }
  .contact-list {
    position: absolute;
    left: 535px;
    top: 312px;
    margin: 0;
    padding: 0;
    list-style: none;
    font-size: 17px;
    color: var(--text-muted);
    line-height: 1.4;
    white-space: nowrap;
  }
  .contact-item {
    position: relative;
    padding-left: 28px;
    margin-bottom: 3px;
  }
  .contact-icon {
    position: absolute;
    left: 0;
    top: 4px;
  }
</style>
</head>
<body>
<div class="canvas">
  <section class="business-card">
    <div class="brand">
      <span class="brand-mark"></span>
      <span class="brand-name">Velvet Compass</span>
    </div>
    <div class="brand-tagline">Lifestyle and Dating Specialists</div>

    <div class="person">
      <svg class="person-marker" width="26" height="22" viewBox="0 0 26 22" aria-hidden="true">
        <polygon points="0,0 26,11 0,22" fill="var(--accent-orange)"/>
      </svg>
      <p class="person-name">Ted</p>
      <p class="person-title">Dating Instructor</p>
    </div>

    <ul class="contact-list">
      <li class="contact-item">
        <svg class="contact-icon" width="16" height="16" viewBox="0 0 16 16" aria-hidden="true"><circle cx="8" cy="8" r="8" fill="var(--accent-red)"/><path d="M8 3.5a3 3 0 0 0-3 3c0 2.2 3 5.5 3 5.5s3-3.3 3-5.5a3 3 0 0 0-3-3z" fill="#fff"/></svg>
        4872 Marlow Terrace, #9<br>Miami Beach, FL 33139
      </li>
      <li class="contact-item">
        <svg class="contact-icon" width="16" height="16" viewBox="0 0 16 16" aria-hidden="true"><circle cx="8" cy="8" r="8" fill="var(--accent-red)"/><path d="M5 4.5l1.5-.5 1 2-1 .8a5 5 0 0 0 2.7 2.7l.8-1 2 1-.5 1.5c-3.5.3-6.8-3-6.5-6.5z" fill="#fff"/></svg>
        561-204-8817
      </li>
      <li class="contact-item">
        <svg class="contact-icon" width="16" height="16" viewBox="0 0 16 16" aria-hidden="true"><circle cx="8" cy="8" r="8" fill="var(--accent-red)"/><rect x="4" y="5" width="8" height="6" fill="#fff"/><path d="M4 5l4 3 4-3" stroke="var(--accent-red)" stroke-width="1" fill="none"/></svg>
        Skyheron@velvetcompasslife.com
      </li>
      <li class="contact-item">
        <svg class="contact-icon" width="16" height="16" viewBox="0 0 16 16" aria-hidden="true"><circle cx="8" cy="8" r="8" fill="var(--accent-red)"/><circle cx="8" cy="8" r="4" fill="none" stroke="#fff" stroke-width="1.2"/><line x1="4" y1="8" x2="12" y2="8" stroke="#fff" stroke-width="1"/></svg>
        www.velvetcompasslife.com
      </li>
    </ul>

    <aside class="side-strip">
      <div class="side-strip-line"></div>
      <div class="side-strip-url">www.velvetcompasslife.com</div>
    </aside>
  </section>
</div>
</body>
</html>
```